Bref créative
Business Card design for Property Management Company
Harborlight Stewards
Professional
Corwin Talbot
P.O. Box K-4183
Nassau, Bahamas
corwin@harborlightstewardsgroup.com

```html
<!DOCTYPE html>
<html lang="en">
<head>
<meta charset="utf-8">
<title>Harborlight Stewards — Stationery</title>
<link href="https://fonts.googleapis.com/css2?family=Cinzel:wght@500&family=Lato:wght@400;700&display=swap" rel="stylesheet">
<style>
  :root {
    --bg: #eeeff1;
    --paper: #ffffff;
    --navy: #0d3d73;
    --blue: #1c64a6;
    --sky: #3a8fd0;
    --ink: #1f3552;
    --muted: #7a8594;
    --faint: #e6eef6;
  }
  * { margin: 0; padding: 0; box-sizing: border-box; }
  html, body { width: 1200px; height: 936px; overflow: hidden; background: var(--bg); }
  .canvas { position: relative; width: 1200px; height: 936px; }
  .sheet {
    position: absolute; background: var(--paper); overflow: hidden;
    box-shadow: 0 2px 6px rgba(0,0,0,0.12);
  }
  .sheet svg.swoosh { position: absolute; inset: 0; width: 100%; height: 100%; }
  .brand { position: absolute; display: flex; align-items: center; gap: 8px; }
  .brand .dot { border-radius: 50%; background: var(--blue); flex: none; }
  .brand .name {
    font-family: "Cinzel", serif; font-weight: 500; color: var(--ink);
    line-height: 1.05; letter-spacing: 0.04em;
  }
  .small { font-family: "Lato", sans-serif; color: var(--muted); }

  .letterhead { left: 182px; top: 63px; width: 387px; height: 544px; }
  .letterhead .brand { left: 22px; top: 36px; }
  .letterhead .dot { width: 26px; height: 26px; }
  .letterhead .name { font-size: 13px; }
  .letterhead .mark-faint {
    position: absolute; left: 106px; top: 236px; width: 104px; height: 104px;
    border-radius: 50%; background: var(--faint);
  }
  .letterhead .contact { position: absolute; left: 22px; bottom: 30px; font-size: 6.5px; line-height: 1.6; }

  .folder { left: 633px; top: 43px; width: 458px; height: 572px; }
  .folder .brand { left: 70px; top: 256px; gap: 14px; }
  .folder .dot { width: 60px; height: 60px; }
  .folder .name { font-size: 30px; }

  .card-front { left: 46px; top: 653px; width: 174px; height: 104px; }
  .card-front .brand { left: 10px; top: 12px; gap: 5px; }
  .card-front .dot { width: 14px; height: 14px; }
  .card-front .name { font-size: 7px; }
  .card-front .person { position: absolute; left: 12px; top: 44px; font-size: 6px; line-height: 1.5; }
  .card-front .person strong { color: var(--ink); font-weight: 700; }

  .card-back { left: 46px; top: 772px; width: 174px; height: 104px; background: var(--blue); }
  .card-back .brand { left: 0; right: 0; top: 0; bottom: 0; justify-content: center; gap: 6px; }
  .card-back .dot { width: 26px; height: 26px; background: #f4b43a; }
  .card-back .name { font-size: 8px; color: #ffffff; }

  .envelope-front { left: 261px; top: 665px; width: 435px; height: 211px; }
  .envelope-front .brand { left: 26px; top: 34px; gap: 10px; }
  .envelope-front .dot { width: 34px; height: 34px; }
  .envelope-front .name { font-size: 15px; }
  .envelope-front .address { position: absolute; left: 72px; top: 78px; font-size: 6px; }

  .envelope-back { left: 739px; top: 665px; width: 420px; height: 211px; }
  .envelope-back .web {
    position: absolute; left: 0; right: 0; top: 26px; text-align: center;
    font-family: "Lato", sans-serif; font-size: 9px; letter-spacing: 0.08em; color: #ffffff;
  }
</style>
</head>
<body>
<main class="canvas">

  <svg width="0" height="0" style="position:absolute">
    <defs>
      <linearGradient id="band" x1="0" y1="0" x2="1" y2="0">
        <stop offset="0" stop-color="#2a7cc2"/>
        <stop offset="1" stop-color="#0d3d73"/>
      </linearGradient>
    </defs>
  </svg>

  <section class="sheet letterhead">
    <svg class="swoosh" viewBox="0 0 387 544" preserveAspectRatio="none">
      <path d="M262 0 Q350 272 292 544" fill="none" stroke="var(--sky)" stroke-width="5"/>
      <path d="M296 0 L387 0 L387 544 L318 544 Q390 272 296 0 Z" fill="url(#band)"/>
    </svg>
    <div class="brand"><span class="dot"></span><span class="name">Harborlight<br>Stewards</span></div>
    <div class="mark-faint"></div>
    <div class="contact small">
      P.O. Box K-4183<br>Nassau, Bahamas<br>Tel 242 555 0148<br>Fax 242 555 0149<br>corwin@harborlightstewardsgroup.com
    </div>
  </section>

  <section class="sheet folder">
    <svg class="swoosh" viewBox="0 0 458 572" preserveAspectRatio="none">
      <path d="M332 0 Q430 286 368 572" fill="none" stroke="var(--sky)" stroke-width="6"/>
      <path d="M366 0 L458 0 L458 572 L392 572 Q470 286 366 0 Z" fill="url(#band)"/>
    </svg>
    <div class="brand"><span class="dot"></span><span class="name">Harborlight<br>Stewards</span></div>
  </section>

  <section class="sheet card-front">
    <svg class="swoosh" viewBox="0 0 174 104" preserveAspectRatio="none">
      <path d="M128 0 Q160 52 140 104" fill="none" stroke="var(--sky)" stroke-width="2"/>
      <path d="M140 0 L174 0 L174 104 L150 104 Q176 52 140 0 Z" fill="url(#band)"/>
    </svg>
    <div class="brand"><span class="dot"></span><span class="name">Harborlight<br>Stewards</span></div>
    <div class="person small"><strong>Corwin Talbot</strong><br>Managing Director<br>Tel 242 555 0148<br>corwin@harborlightstewardsgroup.com</div>
  </section>

  <section class="sheet card-back">
    <div class="brand"><span class="dot"></span><span class="name">Harborlight<br>Stewards</span></div>
  </section>

  <section class="sheet envelope-front">
    <svg class="swoosh" viewBox="0 0 435 211" preserveAspectRatio="none">
      <path d="M366 0 Q410 106 386 211" fill="none" stroke="var(--sky)" stroke-width="3"/>
      <path d="M384 0 L435 0 L435 211 L398 211 Q432 106 384 0 Z" fill="url(#band)"/>
    </svg>
    <div class="brand"><span class="dot"></span><span class="name">Harborlight<br>Stewards</span></div>
    <div class="address small">P.O. Box K-4183 · Nassau, Bahamas</div>
  </section>

  <section class="sheet envelope-back">
    <svg class="swoosh" viewBox="0 0 420 211" preserveAspectRatio="none">
      <path d="M0 0 L420 0 L420 52 Q210 74 0 52 Z" fill="url(#band)"/>
      <path d="M0 60 Q210 82 420 60" fill="none" stroke="var(--sky)" stroke-width="2"/>
    </svg>
    <div class="web">WWW.HARBORLIGHTSTEWARDSGROUP.COM</div>
  </section>

</main>
</body>
</html>
```